Dental clinic brochure design (Z fold)

We need a new brochure design made for our dental clinic - Brindlemoor Dental Surgery. One side is in English, the other is in Vietnamese - all text and translations provided in brochure sample with further instructions in word doc. We require a brochure design in a Z fold to convey a family friendly dental clinic, incorporating our logo colour into the theme and designers choice on complimentary colours. Additional high quality images are provided for use if required or free to use own images.

Colors
33b8a4
00a990
86cfc6

Requirements
Must have
• Easy to read font, flows from text to pictures and page to page
• At least 2 dental images

```html
<!DOCTYPE html>
<html lang="vi">
<head>
<meta charset="UTF-8">
<title>Brindlemoor Dental Surgery – Brochure</title>
<link href="https://fonts.googleapis.com/css2?family=Cinzel:wght@400;700&family=Crimson+Pro:ital,wght@0,400;1,400;1,700&display=swap" rel="stylesheet">
<style>
  :root {
    --teal: #33b8a4;
    --teal-deep: #00a990;
    --teal-soft: #86cfc6;
    --slate: #5f5f5f;
    --ink: #555555;
    --text-grey: #6a6a6a;
    --paper: #ffffff;
  }
  * { margin: 0; padding: 0; box-sizing: border-box; }
  html, body { width: 1200px; height: 716px; overflow: hidden; background: var(--paper); }
  .brochure { position: relative; width: 1200px; height: 716px; font-family: "Crimson Pro", Georgia, serif; }
  .photo { position: absolute; }
  .photo--aligner { left: 170px; top: 0; width: 304px; height: 230px;
    background: linear-gradient(160deg, #f3ece8 0%, #eac9bd 55%, #d9a89a 100%); }
  .photo--before { left: 170px; top: 233px; width: 146px; height: 157px;
    background: linear-gradient(180deg, #d6a48f 0%, #c9807a 50%, #e2c9a0 100%); }
  .photo--after { left: 318px; top: 233px; width: 156px; height: 157px;
    background: linear-gradient(180deg, #e4b7a4 0%, #d98d88 50%, #f4f1ec 100%); }
  .photo--patient { left: 793px; top: 188px; width: 300px; height: 289px;
    background: linear-gradient(135deg, #6fa8d6 0%, #9fdbe0 45%, #f0d2bd 75%, #c9855a 100%); }
  .photo--kids { left: 490px; top: 525px; width: 283px; height: 191px;
    background: linear-gradient(180deg, #f5f5f5 0%, #e9c3a5 40%, #f2c94c 75%, #e84c3d 100%);
    border-radius: 60px 60px 0 0; }

  .promo-title { position: absolute; left: 170px; top: 402px; width: 304px; text-align: center;
    font-family: "Cinzel", serif; font-weight: 700; color: var(--teal-deep);
    font-size: 30px; line-height: 29px; }
  .promo-copy { position: absolute; left: 170px; width: 304px; text-align: center;
    color: var(--text-grey); font-size: 16.5px; line-height: 22px; }
  .promo-copy--exam { top: 488px; }
  .promo-copy--whitening { top: 549px; }
  .promo-note { position: absolute; left: 170px; top: 650px; width: 304px; text-align: center;
    color: var(--teal-deep); font-style: italic; font-size: 19px; }

  .scheme { position: absolute; left: 490px; top: 0; width: 283px; height: 334px; background: var(--slate); }
  .scheme-title { position: absolute; top: 88px; width: 100%; text-align: center;
    font-family: "Cinzel", serif; font-weight: 700; color: var(--teal); font-size: 29px; line-height: 32px; }
  .scheme-subtitle { position: absolute; top: 122px; width: 100%; text-align: center;
    font-family: "Cinzel", serif; color: #fff; font-size: 19px; letter-spacing: 3.5px; }
  .scheme-copy { position: absolute; top: 191px; left: 20px; right: 20px; text-align: center;
    color: #fff; font-size: 17px; line-height: 22px; }
  .scheme-copy em { font-weight: 700; }
  .contact-band { position: absolute; left: 490px; top: 334px; width: 283px; height: 141px; background: var(--teal); }
  .band-disc { position: absolute; left: 612px; top: 317px; width: 44px; height: 44px; border-radius: 50%; background: var(--slate); }
  .contact-copy { position: absolute; top: 52px; width: 100%; text-align: center; color: #fff; font-size: 17px; line-height: 22px; }

  .brand { position: absolute; left: 800px; top: 30px; width: 320px; text-align: center; color: var(--ink);
    font-family: "Cinzel", serif; font-weight: 400; }
  .brand-dot { width: 36px; height: 36px; border-radius: 50%; background: var(--teal); margin: 0 auto 18px; }
  .brand-name { font-size: 24px; letter-spacing: 6px; line-height: 26px; }
  .brand-sub { font-size: 11px; letter-spacing: 7px; margin-top: 6px; }

  .contact-row { position: absolute; left: 812px; display: flex; align-items: center; gap: 14px;
    font-family: "Cinzel", serif; font-weight: 700; color: var(--ink); }
  .contact-row--address { top: 540px; font-size: 16px; letter-spacing: 2px; line-height: 20px; }
  .contact-row--phone { top: 602px; font-size: 20px; letter-spacing: 6px; }
  .contact-row svg { flex: none; }
</style>
</head>
<body>
<main class="brochure">
  <div class="photo photo--aligner" role="img" aria-label="Smiling woman holding a clear aligner tray"></div>
  <div class="photo photo--before" role="img" aria-label="Smile before teeth whitening"></div>
  <div class="photo photo--after" role="img" aria-label="Smile after teeth whitening"></div>

  <h2 class="promo-title">Special<br>Promotions</h2>
  <p class="promo-copy promo-copy--exam">Khám răng, chụp hình x-ray và clean<br>răng chỉ nhận bảo hiểm**</p>
  <p class="promo-copy promo-copy--whitening">Giá Đặc biệt 1 Bộ Tẩy Trắng Răng<br>$199 thông thường là $395</p>
  <p class="promo-note">**Gọi nhân viên để biết thêm</p>

  <section class="scheme">
    <h1 class="scheme-title">CHILD DENTAL</h1>
    <p class="scheme-subtitle">Benefits Scheme</p>
    <p class="scheme-copy">Chúng tôi nhận chương trình<br><em>KidSmile $1000</em> mỗi 2 năm cho<br>thiếu nhi tuổi từ 2 đến 17.</p>
  </section>
  <section class="contact-band">
    <p class="contact-copy">Xin vui lòng liên lạc văn phòng số đt<br>(03) 9000 4821</p>
  </section>
  <div class="band-disc"></div>

  <div class="photo photo--kids" role="img" aria-label="Group of children brushing their teeth"></div>

  <div class="brand">
    <div class="brand-dot"></div>
    <div class="brand-name">BRINDLEMOOR</div>
    <div class="brand-sub">DENTAL SURGERY</div>
  </div>

  <div class="photo photo--patient" role="img" aria-label="Young girl giving a thumbs up in the dental chair"></div>

  <div class="contact-row contact-row--address">
    <svg width="32" height="34" viewBox="0 0 32 34" aria-hidden="true">
      <ellipse cx="16" cy="28" rx="14" ry="4" fill="none" stroke="#86cfc6" stroke-width="2"/>
      <path d="M16 29 C10 20 7 16 7 11 A9 9 0 0 1 25 11 C25 16 22 20 16 29 Z" fill="#86cfc6"/>
      <circle cx="16" cy="11" r="3.5" fill="#fff"/>
    </svg>
    <span>48 Larchfield Rd,<br>Elmview, VIC 3990</span>
  </div>
  <div class="contact-row contact-row--phone">
    <svg width="32" height="32" viewBox="0 0 32 32" aria-hidden="true">
      <circle cx="16" cy="16" r="14" fill="none" stroke="#86cfc6" stroke-width="2.5"/>
      <path d="M11 9 L14 9 L15 13 L13 14.5 C14 17 15.5 18.5 18 19.5 L19.5 17.5 L23 18.5 L23 21.5 C23 22.5 22 23 21 23 C14.5 22.5 9.5 17.5 9 11 C9 10 10 9 11 9 Z" fill="#86cfc6"/>
    </svg>
    <span>(03) 9000 4821</span>
  </div>
</main>
</body>
</html>
```